QUICK: Fresh Ideas for New Home Page Design!

Simply improve on our home page design and provide PSD file.

We are Sunward Coverage, a trusted health insurance comparison site to make shopping and enrolling in Carewell easy. We are certified agents for Pacific Shield Exchange, the state's health insurance marketplace (logo attached).

Use flat UI colors.

Looking for a fun design. Reference websites are:
www.plumvista.com
www.hibrindle.com
www.tolmex.com
www.findcanopy.com
www.trymeadowcoverplan.com

Target Market(s)

Individuals ages 18 - 64 shopping for health insurance for themselves and/or their family members. California residents. Don't have health insurance and want it or have it and looking to change.

Industry/Entity Type

Shopping

Font styles to use
Sans Serif

Colors
faed22
33a6d7
33b7a4

Requirements
Must have
• No stock photos. No medical or doctor images or photos. Use images of families. Friendly. Modern fonts and flat UI colors.
Nice to have
• Create a mock-up logo for Sunward Coverage.
Should not have
• No stock looking photos or images

```html
<!DOCTYPE html>
<html lang="en">
<head>
<meta charset="utf-8">
<title>Sunward Coverage – Home</title>
<link href="https://fonts.googleapis.com/css2?family=Alfa+Slab+One&family=Montserrat:wght@400;600;700&family=Open+Sans:wght@400;600;700&display=swap" rel="stylesheet">
<style>
:root{
  --teal:#1fb5cc;
  --teal-dark:#12899a;
  --hero-box:#0f6f7d;
  --blue:#0a77cf;
  --blue-deep:#085ea5;
  --heading-blue:#1a73c8;
  --orange:#ff9300;
  --cyan:#08a8cc;
  --ink:#333;
  --grey:#666;
  --rule:#bbb;
  --footer:#40444d;
  --footer-text:#c9ccd2;
  --base:#111;
  --white:#fff;
}
*{margin:0;padding:0;box-sizing:border-box}
html,body{width:1200px;height:1000px;overflow:hidden;background:var(--white)}
body{position:relative;font-family:"Open Sans",Arial,sans-serif;color:var(--ink)}
.abs{position:absolute}

/* header */
.top-rule{left:0;top:0;width:1200px;height:2px;background:var(--teal)}
.brand{display:flex;align-items:center;gap:10px}
.brand-dot{width:40px;height:40px;border-radius:50%;background:var(--teal)}
.brand-name{font-family:"Montserrat",sans-serif;font-weight:700;font-size:17px;letter-spacing:2px;color:#3d4a55;line-height:1.1}
.header-brand{left:172px;top:12px}
.utility{left:772px;top:6px;font-family:"Montserrat",sans-serif;font-size:7.5px;color:#666;letter-spacing:.4px;word-spacing:3px}
.utility span{margin-right:16px}

.nav{left:0;top:66px;width:1200px;height:22px;background:var(--teal)}
.nav ul{list-style:none}
.nav li{position:absolute;top:0;font-family:"Montserrat",sans-serif;font-size:11.5px;color:var(--white);line-height:22px;letter-spacing:.3px;white-space:nowrap}
.nav li.active{background:var(--teal-dark);width:94px;text-align:center}

/* hero */
.hero{left:0;top:88px;width:1200px;height:182px;background:linear-gradient(100deg,#c99a82 0%,#3c8fc4 35%,#1f70b8 55%,#d7a88d 75%,#2f7cc0 100%)}
.hero-title{left:231px;top:117px;width:737px;height:30px;background:var(--hero-box);opacity:.92;color:var(--white);font-family:"Montserrat",sans-serif;font-weight:700;font-size:21px;letter-spacing:3.5px;text-align:center;line-height:30px;white-space:nowrap}
.hero-sub{left:300px;top:157px;width:600px;text-align:center;color:var(--white);font-family:"Montserrat",sans-serif;font-weight:700;font-size:17px;letter-spacing:1.5px;line-height:14px}
.hero-btn{left:537px;top:205px;width:134px;height:22px;background:var(--teal-dark);color:var(--white);font-family:"Montserrat",sans-serif;font-size:12px;letter-spacing:.5px;text-align:center;line-height:22px}
.arrow{top:157px}

/* features */
.main-heading{left:0;top:289px;width:1200px;text-align:center;font-family:"Montserrat",sans-serif;font-weight:400;font-size:16px;color:var(--heading-blue);letter-spacing:1.2px}
.dots{height:0;border-top:1px dashed #333}
.feature{top:332px;width:276px;text-align:center}
.feature-icon{display:block;margin:0 auto;width:132px;height:58px}
.feature h3{font-family:"Montserrat",sans-serif;font-weight:400;font-size:11.5px;color:var(--orange);margin-top:7px;letter-spacing:.8px}
.feature p{font-size:10px;line-height:10.5px;color:var(--grey);margin:4px auto 0;width:256px;height:33px;overflow:hidden;font-family:Arial,sans-serif;letter-spacing:.3px}
.feature .more{font-size:9px;color:var(--grey);margin-top:3px;font-family:Arial,sans-serif}
.feature .rule{margin-top:9px;height:1px;background:var(--rule)}
.feature .rule.accent{background:var(--orange)}

/* welcome band */
.band{left:0;top:505px;width:1200px;height:166px;background:var(--blue)}
.services-panel{left:757px;top:505px;width:277px;height:166px;background:var(--blue-deep)}
.welcome-title{left:167px;top:521px;font-family:"Montserrat",sans-serif;font-weight:400;font-size:19px;color:var(--white);letter-spacing:1.8px}
.welcome-lead{left:168px;top:549px;width:600px;color:var(--white);font-weight:700;font-size:9.5px;line-height:10px;font-family:Arial,sans-serif;letter-spacing:.45px}
.welcome-body{left:168px;top:575px;width:565px;color:#d9e9f8;font-size:8.5px;line-height:9px;font-family:Arial,sans-serif;letter-spacing:.25px}
.welcome-btn{left:166px;top:641px;width:127px;height:17px;background:var(--blue-deep);color:var(--white);font-size:8.5px;text-align:center;line-height:17px;font-family:Arial,sans-serif}
.services-title{left:757px;top:521px;width:277px;text-align:center;font-family:"Montserrat",sans-serif;font-weight:700;font-size:14px;color:var(--white);letter-spacing:1.2px}
.services-list{left:792px;top:551px;list-style:none}
.services-list li{font-size:8.5px;line-height:11.8px;color:#d9e9f8;font-family:Arial,sans-serif;padding-left:25px;position:relative;letter-spacing:.3px}
.services-list li::before{content:"";position:absolute;left:0;top:4px;width:7px;height:4px;border-radius:2px;background:#0a3f70}

/* special */
.special-title{left:166px;top:694px;font-family:"Alfa Slab One",serif;font-size:52px;letter-spacing:2px;color:var(--orange);line-height:56px}
.special-lines{left:167px;top:757px;font-family:"Alfa Slab One",serif;font-size:16.5px;line-height:19px;color:#222;letter-spacing:1px}
.special-btn{left:167px;top:806px;width:319px;height:27px;background:var(--orange);color:var(--white);font-family:"Montserrat",sans-serif;font-size:13px;letter-spacing:1px;text-align:center;line-height:27px}
.special-badge{left:762px;top:713px;width:248px;height:105px;border-radius:50%;background:var(--cyan)}

/* footer */
.footer{left:0;top:863px;width:1200px;height:115px;background:var(--footer)}
.f-head{font-family:"Montserrat",sans-serif;font-weight:700;font-size:8px;color:var(--orange);letter-spacing:.4px}
.f-links{list-style:none;font-size:8px;line-height:10px;color:var(--footer-text);font-family:Arial,sans-serif}
.blog-entry{width:195px;font-size:8px;line-height:8.5px;color:var(--footer-text);font-family:Arial,sans-serif}
.blog-entry em{display:block;font-size:6.5px;color:#e2e4e8}
.blog-more{left:538px;top:959px;font-size:8px;color:var(--white);text-decoration:underline;font-family:Arial,sans-serif}
.footer-brand{left:762px;top:882px}
.footer-brand .brand-dot{width:28px;height:28px}
.footer-brand .brand-name{font-size:11px;color:#8a929c;letter-spacing:1.5px}
.address{left:758px;top:917px;width:200px}
.address p{font-size:7.5px;line-height:8.5px;color:var(--footer-text);font-family:Arial,sans-serif;margin-top:3px}
.contact{display:flex;align-items:center;gap:8px;font-size:7px;color:var(--footer-text);font-family:Arial,sans-serif}

.base{left:0;top:978px;width:1200px;height:22px;background:var(--base)}
.copyright{left:166px;top:985px;font-size:7px;color:#bbb;font-family:Arial,sans-serif}
.licence{left:537px;top:979px;font-family:"Montserrat",sans-serif;font-weight:700;font-size:17px;color:var(--white);letter-spacing:2.6px}
.social{left:879px;top:983px;display:flex;gap:5px}
.social span{width:26px;height:12px;border-radius:6px;background:var(--orange)}
</style>
</head>
<body>

<div class="abs top-rule"></div>
<div class="abs brand header-brand">
  <span class="brand-dot"></span>
  <span class="brand-name">SUNWARD<br>COVERAGE</span>
</div>
<div class="abs utility"><span>LANGUAGES: ENGLISH</span>LOGIN / REGISTER</div>

<nav class="abs nav">
  <ul>
    <li class="active" style="left:168px">HOME</li>
    <li style="left:284px">ABOUT US</li>
    <li style="left:408px">COVERAGE</li>
    <li style="left:536px">RESOURCES</li>
    <li style="left:672px">PROGRAMS &amp; PARTNERS</li>
    <li style="left:907px">NEWS CENTER</li>
  </ul>
</nav>

<section>
  <div class="abs hero" role="img" aria-label="Photo of a smiling family of three: mother, child and father"></div>
  <h1 class="abs hero-title">WE HAVE THE HEALTH PLAN FOR YOU.</h1>
  <p class="abs hero-sub">lorem ipsume dolor sit is lorem ipsume<br>dolor sit dummy text</p>
  <div class="abs hero-btn">VIEW MORE</div>
  <svg class="abs arrow" style="left:22px" width="26" height="34" viewBox="0 0 26 34"><path d="M22 2 L5 17 L22 32" fill="none" stroke="#fff" stroke-width="2"/></svg>
  <svg class="abs arrow" style="left:1150px" width="26" height="34" viewBox="0 0 26 34"><path d="M4 2 L21 17 L4 32" fill="none" stroke="#fff" stroke-width="2"/></svg>
</section>

<h2 class="abs main-heading">SOME MAIN HEADING GOES HERE</h2>
<div class="abs dots" style="left:528px;top:310px;width:128px"></div>

<article class="abs feature" style="left:166px">
  <svg class="feature-icon" viewBox="0 0 132 58"><ellipse cx="66" cy="29" rx="65" ry="28" fill="#ff9300"/><circle cx="66" cy="24" r="11" fill="#fff"/><rect x="60" y="33" width="12" height="9" rx="2" fill="#fff"/><path d="M66 18 L62 26 L69 25 L65 33" fill="none" stroke="#ff9300" stroke-width="2"/></svg>
  <h3>HEADING GOES HERE</h3>
  <p>Lorem Ipsum is simply dummy text of the printing and typesetting industry. Lorem Ipsum has been the industry's standard</p>
  <div class="more">[ Read More ]</div>
  <div class="rule accent"></div>
</article>
<article class="abs feature" style="left:462px">
  <svg class="feature-icon" viewBox="0 0 132 58"><ellipse cx="66" cy="29" rx="65" ry="28" fill="#fff" stroke="#ccc"/><path d="M66 40 C50 30 52 18 60 18 C64 18 66 22 66 22 C66 22 68 18 72 18 C80 18 82 30 66 40 Z" fill="#ff9300"/><path d="M46 30 Q50 44 66 44 Q82 44 86 30" fill="none" stroke="#ff9300" stroke-width="4"/></svg>
  <h3>HEADING GOES HERE</h3>
  <p>Lorem Ipsum is simply dummy text of the printing and typesetting industry. Lorem Ipsum has been the industry's</p>
  <div class="more">[ Read More ]</div>
  <div class="rule"></div>
</article>
<article class="abs feature" style="left:757px">
  <svg class="feature-icon" viewBox="0 0 132 58"><ellipse cx="66" cy="29" rx="65" ry="28" fill="#fff" stroke="#ccc"/><rect x="36" y="22" width="14" height="14" fill="#ff9300"/><rect x="82" y="22" width="14" height="14" fill="#ff9300"/><path d="M50 26 L64 24 L82 26 L82 33 L68 40 L50 33 Z" fill="#ff9300"/></svg>
  <h3>HEADING GOES HERE</h3>
  <p>Lorem Ipsum is simply dummy text of the printing and typesetting industry. Lorem Ipsum has been the industry's standard</p>
  <div class="more">[ Read More ]</div>
  <div class="rule"></div>
</article>

<section>
  <div class="abs band"></div>
  <div class="abs services-panel"></div>
  <h2 class="abs welcome-title">WELCOME TO OUR SITE</h2>
  <p class="abs welcome-lead">Lorem Ipsum is simply dummy text of the printing and typesetting industry<br>Lorem Ipsum has been the industry's standard dummy text ever since.</p>
  <p class="abs welcome-body">Lorem Ipsum is simply dummy text of the printing and typesetting industry. Lorem Ipsum has been the industry's standard dummy text ever since. Lorem Ipsum is simply dummy text of the printing and typesetting industry. Lorem Ipsum has been the industry's standard dummy text ever since. Lorem Ipsum is simply dummy text of the printing and typesetting industry. Lorem Ipsum has been the industry's standard dummy text ever since. Lorem Ipsum is simply dummy text of the printing and typesetting industry. Lorem Ipsum has been the industry's standard dummy text ever since.</p>
  <div class="abs welcome-btn">Read More [+]</div>
  <h2 class="abs services-title">OUR SERVICES</h2>
  <div class="abs dots" style="left:858px;top:540px;width:74px;border-color:#fff"></div>
  <ul class="abs services-list">
    <li>Lorem Ipsum has</li>
    <li>been the industry's standard</li>
    <li>dummy text ever since.</li>
    <li>Lorem Ipsum is simply</li>
    <li>dummy text</li>
    <li>Lorem Ipsum has</li>
    <li>been the industry's standard</li>
    <li>dummy text ever since.</li>
    <li>Lorem Ipsum is simply</li>
  </ul>
</section>

<section>
  <h2 class="abs special-title">Special</h2>
  <p class="abs special-lines">some EXTRA<br>big text line goes here</p>
  <div class="abs special-btn">SOME HEADING HERE</div>
  <div class="abs special-badge" role="img" aria-label="Illustration of two hands holding a house"></div>
</section>

<footer>
  <div class="abs footer"></div>
  <h4 class="abs f-head" style="left:168px;top:877px">QUICK LINK</h4>
  <ul class="abs f-links" style="left:168px;top:894px"><li>Home</li><li>About us</li><li>Services</li><li>Packages</li><li>FAQ</li><li>Contact</li></ul>
  <ul class="abs f-links" style="left:285px;top:894px"><li>Home</li><li>About us</li><li>Services</li><li>Packages</li><li>FAQ</li><li>Contact</li></ul>
  <ul class="abs f-links" style="left:407px;top:894px"><li>Home</li><li>About us</li><li>Services</li><li>Packages</li><li>FAQ</li><li>Contact</li></ul>

  <h4 class="abs f-head" style="left:537px;top:877px">BLOG</h4>
  <div class="abs blog-entry" style="left:537px;top:895px">Lorem Ipsum has been the industry's standard dummy text<em>- Mara Quill &nbsp;&nbsp;&nbsp;&nbsp; 15 Dec 2013</em></div>
  <div class="abs blog-entry" style="left:537px;top:928px">Lorem Ipsum has been the industry's standard dummy text<em>- Mara Quill &nbsp;&nbsp;&nbsp;&nbsp; 15 Dec 2013</em></div>
  <div class="abs blog-more">View More</div>

  <div class="abs brand footer-brand">
    <span class="brand-dot"></span>
    <span class="brand-name">SUNWARD<br>COVERAGE</span>
  </div>
  <div class="abs address">
    <h4 class="f-head">ADDRESS</h4>
    <p>Lorem Ipsum has been the industry's standard dummy text</p>
    <div class="contact" style="margin-top:7px">
      <svg width="10" height="9" viewBox="0 0 10 9"><path d="M2 0 L4 2 L3 3.5 Q4.5 6 6.5 6.5 L7.5 5.5 L9.5 7.5 L8 9 Q1 8 0 1.5 Z" fill="#fff"/></svg>1111 1111
    </div>
    <div class="contact" style="margin-top:3px">
      <svg width="10" height="8" viewBox="0 0 10 8"><rect width="10" height="8" rx="1" fill="#fff"/><path d="M0.5 1 L5 4.5 L9.5 1" fill="none" stroke="#40444d" stroke-width="1"/></svg>hello@sunmailbox.net
    </div>
  </div>

  <div class="abs base"></div>
  <p class="abs copyright">Design©2014. All Rights Reserved.</p>
  <p class="abs licence">L.no. A011 22 333 658</p>
  <div class="abs social" aria-label="Social links"><span></span><span></span><span></span><span></span><span></span></div>
</footer>

</body>
</html>
```